New Business Card Design Project for Handyman Business

I would like to purchase a customized version of a design you have previously submitted - https://www.artvelloshowcase.com/design/58172046
I love this design!
I am hoping you can design something similar to this for our Handyman Business.
Attached is our logo and some graphics we have used.
Here is a link to the Google Doc with the content that needs to be included, https://files.quorvandel.net/document/d/e/4QZTR-8kPw2LmXn5Hb7rYcVt-qaaJsK3Df9TgNpU4WeR__LmcXaBvKpHsd2Qjn7wo4tzhgrVb41K85o3ttSTq/pub
Target Market(s)
Real Estate Agents, Home Owners and Property Managers
Industry/Entity Type
Construction/ Speciality Trade
Contact Information for Business Card
https://files.quorvandel.net/document/d/7QwRtYpL_zxkn4BvHnCdFs8TmKjWaEr2LUXPo6cxhg/edit?usp=sharing
Font styles to use
Other font styles liked:
- Ubuntu
Look and feel
Each slider illustrates characteristics of the customer's brand and the style your logo design should communicate.

```html
<!DOCTYPE html>
<html lang="en">
<head>
<meta charset="utf-8">
<title>Brightwell Business Card</title>
<link rel="stylesheet" href="https://fonts.googleapis.com/css2?family=Arimo:wght@400;700&family=Ubuntu:wght@500&display=swap">
<style>
  :root {
    --stage: #2a2a2a;
    --card: #161616;
    --card-pattern-a: #1d1d1d;
    --card-pattern-b: #151515;
    --green: #45b649;
    --blue: #1f77c9;
    --orange: #ee6a2c;
    --white: #f4f4f4;
  }
  * { box-sizing: border-box; margin: 0; padding: 0; }
  html, body { width: 1200px; height: 875px; overflow: hidden; }
  body {
    background: var(--stage);
    font-family: "Arimo", Arial, sans-serif;
    position: relative;
  }
  .card {
    position: absolute;
    top: 130px;
    width: 350px;
    height: 615px;
    background: var(--card);
    border-radius: 30px;
    overflow: hidden;
  }
  .card--front { left: 205px; }
  .card--back { left: 645px; }

  /* Front */
  .brand {
    position: absolute;
    top: 120px;
    left: 0; right: 0;
    text-align: center;
  }
  .brand-row {
    display: inline-flex;
    align-items: center;
    gap: 10px;
  }
  .brand-square {
    width: 30px; height: 30px;
    background: var(--blue);
  }
  .brand-name {
    font-family: "Ubuntu", sans-serif;
    font-weight: 500;
    font-size: 46px;
    color: var(--green);
    letter-spacing: -0.5px;
  }
  .brand-tagline {
    margin-top: 6px;
    font-size: 12px;
    font-weight: 700;
    letter-spacing: 3px;
    color: var(--orange);
  }
  .person {
    position: absolute;
    top: 278px;
    left: 0; right: 0;
    text-align: center;
  }
  .person-name {
    font-size: 28px;
    font-weight: 700;
    color: var(--green);
    letter-spacing: 0.5px;
  }
  .person-title {
    font-size: 18px;
    color: var(--blue);
    margin-top: 2px;
  }
  .icon-rule {
    position: absolute;
    top: 355px;
    left: 36px; right: 36px;
    display: flex;
    align-items: center;
    gap: 8px;
  }
  .icon-rule .rule { flex: 1; height: 1px; background: var(--blue); }
  .icon-rule svg { width: 26px; height: 26px; display: block; }
  .contact {
    position: absolute;
    top: 398px;
    left: 0; right: 0;
    text-align: center;
    color: var(--white);
    font-size: 16px;
    line-height: 25px;
  }
  .divider {
    position: absolute;
    top: 488px;
    left: 36px; right: 36px;
    height: 1px;
    background: var(--blue);
  }
  .services {
    position: absolute;
    top: 506px;
    left: 0; right: 0;
    text-align: center;
    color: var(--white);
    font-size: 16px;
    line-height: 28px;
  }
  .services .dot { color: var(--orange); margin: 0 4px; }

  /* Back */
  .pattern-field {
    position: absolute;
    top: 0; left: 0; right: 0;
    height: 440px;
    background: linear-gradient(160deg, var(--card-pattern-a), var(--card-pattern-b));
  }
  .back-mark {
    position: absolute;
    top: 262px;
    left: 155px;
    width: 40px; height: 40px;
    background: var(--blue);
  }
  .social-rule {
    position: absolute;
    top: 478px;
    left: 28px; right: 28px;
    display: flex;
    align-items: center;
    gap: 8px;
  }
  .social-rule .rule { flex: 1; height: 1px; background: var(--orange); }
  .social-dot {
    width: 24px; height: 24px;
    border: 1.5px solid var(--orange);
    border-radius: 50%;
  }
  .hashtag {
    position: absolute;
    top: 520px;
    left: 0; right: 0;
    text-align: center;
    color: var(--green);
    font-size: 16px;
  }
</style>
</head>
<body>
  <section class="card card--front">
    <div class="brand">
      <div class="brand-row">
        <span class="brand-square"></span>
        <span class="brand-name">brightwell</span>
      </div>
      <div class="brand-tagline">HOME CARE SPECIALISTS</div>
    </div>

    <div class="person">
      <div class="person-name">AVERY COLTON</div>
      <div class="person-title">Owner/ Handyman</div>
    </div>

    <div class="icon-rule">
      <span class="rule"></span>
      <svg viewBox="0 0 26 26" aria-label="Phone">
        <circle cx="13" cy="13" r="12" fill="none" stroke="var(--orange)" stroke-width="1.5"/>
        <path d="M9 7.5c.6-.4 1.3-.3 1.6.3l1 2c.2.5.1 1-.3 1.3l-.8.6c.6 1.4 1.5 2.4 2.9 3l.6-.8c.3-.4.9-.5 1.3-.3l2 1c.6.3.7 1 .3 1.6l-.8 1c-.6.7-1.6.9-2.5.5-3-1.3-5.3-3.6-6.6-6.6-.4-.9-.2-1.9.5-2.5z" fill="var(--orange)"/>
      </svg>
      <svg viewBox="0 0 26 26" aria-label="Email">
        <circle cx="13" cy="13" r="12" fill="none" stroke="var(--orange)" stroke-width="1.5"/>
        <rect x="7" y="9" width="12" height="8.5" rx="1" fill="var(--orange)"/>
        <path d="M7.5 9.5 13 14l5.5-4.5" fill="none" stroke="var(--card)" stroke-width="1.2"/>
      </svg>
      <svg viewBox="0 0 26 26" aria-label="Website">
        <circle cx="13" cy="13" r="12" fill="none" stroke="var(--orange)" stroke-width="1.5"/>
        <g fill="none" stroke="var(--orange)" stroke-width="1.2">
          <circle cx="13" cy="13" r="6.5"/>
          <ellipse cx="13" cy="13" rx="2.8" ry="6.5"/>
          <path d="M6.5 13h13M7.5 9.8h11M7.5 16.2h11"/>
        </g>
      </svg>
      <span class="rule"></span>
    </div>

    <div class="contact">
      <div>(555) 014-2290</div>
      <div>avery@brightwell-home.com</div>
      <div>www.brightwell-home.com</div>
    </div>

    <div class="divider"></div>

    <div class="services">
      <div>Commercial and Residential Handyman</div>
      <div>Improve<span class="dot">•</span>Repair<span class="dot">•</span>Remodel<span class="dot">•</span>Maintain</div>
    </div>
  </section>

  <section class="card card--back">
    <div class="pattern-field" role="img" aria-label="Faint repeating brand-mark pattern across the card back"></div>
    <span class="back-mark"></span>

    <div class="social-rule">
      <span class="rule"></span>
      <span class="social-dot"></span>
      <span class="social-dot"></span>
      <span class="social-dot"></span>
      <span class="social-dot"></span>
      <span class="rule"></span>
    </div>
    <div class="hashtag">#BrightwellHandymanServices</div>
  </section>
</body>
</html>
```